Need bold & innovative new PPT design

Our logo/branding is being designed at the moment on this site.We are a Minerals and Mining Industry Association which has mining companies as its members. We do collaborate research with research companies, universities and scientific bodies to bring projects which benefit the mining industry. We are an international company which started 60 years ago and want a renewal/rejuvenation of our brand.

Target Market(s)

Mining & Minerals Industry. Scientists, and scientific research organisations.

Industry/Entity Type

Mining

Requirements
Must have
• Bold designs and colours. I have attached an old version of our template (with dated colours & logo). Please use new logo (attached) and it's colours.
• NOTE: There may be some confusion - we only need 2 slides. The title slide & the normal presentation pages. Thanks
Nice to have
• Red & Blue as according to our new logo and websites are preferred.
• New logo attached. New website: http://quorvane-assoc.net/
Should not have
• Yellow! We're quite sick of that.

```html
<!DOCTYPE html>
<html lang="en">
<head>
<meta charset="utf-8">
<title>Veltara Collective – Presentation Template</title>
<link href="https://fonts.googleapis.com/css2?family=Lato:wght@400;700&family=Tinos:wght@700&display=swap" rel="stylesheet">
<style>
  :root{
    --canvas:#8b8c8e;
    --blue:#1e76c6;
    --blue-deep:#1a2f78;
    --blue-band:#1f74c2;
    --red:#e8262b;
    --ink:#1d1d1d;
    --white:#ffffff;
    --earth-light:#e6c9a6;
    --earth-mid:#c9976a;
    --earth-dark:#9c6a44;
  }
  *{box-sizing:border-box;margin:0;padding:0}
  html,body{width:1200px;height:924px;overflow:hidden;background:var(--canvas)}
  body{position:relative;font-family:"Lato",Arial,sans-serif;color:var(--ink)}

  .slide{position:absolute;background:var(--white);overflow:hidden}
  .slide--title{left:27px;top:27px;width:567px;height:424px;background:var(--blue)}
  .slide--definition{left:611px;top:27px;width:564px;height:424px}
  .slide--overview{left:27px;top:471px;width:567px;height:426px}
  .slide--closing{left:619px;top:475px;width:556px;height:415px}

  /* brand lockup */
  .brand{display:flex;align-items:center;gap:6px;font-weight:700;color:var(--blue-deep);letter-spacing:.5px;white-space:nowrap}
  .brand__dot{width:12px;height:12px;border-radius:50%;background:var(--blue);flex:none}

  /* title slide */
  .photo-grid{position:absolute;left:0;top:0;width:567px;height:226px;
    display:grid;grid-template-columns:repeat(5,1fr);grid-template-rows:1fr 1fr;gap:5px}
  .photo-grid__tile{border-radius:14px;background:linear-gradient(150deg,var(--earth-light),var(--earth-mid) 55%,var(--earth-dark))}
  .photo-grid__tile--logo{grid-column:1 / span 2;grid-row:1;background:var(--white);
    display:flex;align-items:center;padding-left:30px}
  .photo-grid__tile--logo .brand{font-size:17px}
  .title-heading{position:absolute;top:268px;left:172px;width:440px;text-align:center;color:var(--white);font-size:19.5px;font-weight:400}
  .title-slogan{position:absolute;top:300px;left:172px;width:440px;text-align:center;color:var(--white);font-size:14px}
  .title-url{position:absolute;left:0;width:567px;top:400px;text-align:center;color:var(--white);font-size:14px}

  /* shared content-slide parts */
  .page-number{position:absolute;top:17px;width:34px;height:23px;border-radius:4px;background:var(--blue);
    color:var(--white);font-size:12px;display:flex;align-items:center;justify-content:center}
  .slide-heading{position:absolute;font-size:20px;font-weight:400;letter-spacing:.2px}
  .slide-heading__accent{color:var(--red);font-weight:700}
  .footer-band{position:absolute;left:0;right:0;bottom:0;height:49px;
    background:linear-gradient(90deg,var(--blue-deep),var(--blue-band) 45%,var(--blue-band));
    color:var(--white);font-size:13px}
  .footer-band__url{position:absolute;left:0;right:0;top:16px;text-align:center}
  .footer-band__brand{position:absolute;right:32px;top:12px;font-size:12px}
  .footer-band__brand .brand{color:var(--white)}
  .footer-band__brand .brand__dot{width:8px;height:8px;background:var(--white)}

  /* definition slide */
  .slide--definition .page-number{left:492px}
  .slide--definition .slide-heading{left:39px;top:42px}
  .subheading{position:absolute;left:42px;top:87px;font-size:13px;font-weight:700;text-decoration:underline}
  .checklist{position:absolute;left:42px;top:127px;width:500px;list-style:none;font-size:12.3px;line-height:17.5px}
  .checklist__item{position:relative;padding-left:21px;margin-bottom:23px}
  .checklist__item::before{content:"\2713";position:absolute;left:0;top:-1px;font-size:13px}

  /* overview slide */
  .slide--overview .page-number{left:498px}
  .slide--overview .slide-heading{left:34px;top:43px}
  .chart{position:absolute;left:0;top:0}
  .feature{position:absolute;left:336px;width:200px}
  .feature__title{display:flex;align-items:center;gap:12px;font-size:12.5px;font-weight:700}
  .feature__icon{width:11px;height:11px;border-radius:2px}
  .feature__icon--blue{background:var(--blue)}
  .feature__icon--red{background:var(--red)}
  .feature__text{margin:9px 0 0 22px;width:160px;font-size:9.5px;line-height:14px}

  /* closing slide */
  .closing-brand{position:absolute;left:0;right:0;top:60px;display:flex;justify-content:center}
  .closing-brand .brand{font-size:28px}
  .closing-brand .brand__dot{width:16px;height:16px}
  .thank-you{position:absolute;left:0;right:0;top:158px;text-align:center;font-family:"Tinos","Times New Roman",serif;font-size:31px;font-weight:700}
  .presenter{position:absolute;left:0;right:0;top:194px;text-align:center;font-size:12.5px}
  .contact{position:absolute;left:200px;top:238px;font-size:12.5px;line-height:16.8px;font-style:normal}
  .contact__label{font-weight:700}
</style>
</head>
<body>

<section class="slide slide--title">
  <div class="photo-grid" role="img" aria-label="Photo mosaic of a large haul truck on a reddish open-pit mine road">
    <div class="photo-grid__tile photo-grid__tile--logo">
      <div class="brand"><span class="brand__dot"></span>VELTARA COLLECTIVE</div>
    </div>
    <div class="photo-grid__tile"></div><div class="photo-grid__tile"></div><div class="photo-grid__tile"></div>
    <div class="photo-grid__tile"></div><div class="photo-grid__tile"></div><div class="photo-grid__tile"></div>
    <div class="photo-grid__tile"></div><div class="photo-grid__tile"></div>
  </div>
  <h1 class="title-heading">PRESENTATION TITLE COMES HERE</h1>
  <p class="title-slogan">Followed by some slogan comes here</p>
  <p class="title-url">www. quorvane-assoc.net</p>
</section>

<section class="slide slide--definition">
  <div class="page-number">01</div>
  <h2 class="slide-heading">“INNOVATION” <span class="slide-heading__accent">GIRC DEFINITION</span></h2>
  <p class="subheading">Product , Process, Marketing &amp; Organisational Innovation</p>
  <ul class="checklist">
    <li class="checklist__item">… a good or service that is new or significantly improved. This includes significant improvements in technical specifications, components and materials, incorporated software, user friendliness or other functional characteristics.</li>
    <li class="checklist__item">… a new or significantly improved production or delivery method. This includes significant changes in techniques, equipment and/or software.</li>
    <li class="checklist__item">The process of innovation transforms an idea into a new, improved<br>product, process or service. New technology is the visible expression of this.</li>
  </ul>
  <footer class="footer-band">
    <span class="footer-band__url">www. quorvane-assoc.net</span>
    <span class="footer-band__brand"><span class="brand"><span class="brand__dot"></span>VELTARA</span></span>
  </footer>
</section>

<section class="slide slide--overview">
  <div class="page-number">02</div>
  <h2 class="slide-heading">VELTARA COLLECTIVE: <span class="slide-heading__accent">AT GLANCE</span></h2>
  <svg class="chart" width="567" height="300" viewBox="0 0 567 300" aria-label="Bar chart of two series across four categories">
    <g stroke="#d9d9d9" stroke-width="1">
      <line x1="58" y1="107" x2="238" y2="107"/><line x1="58" y1="133.4" x2="238" y2="133.4"/>
      <line x1="58" y1="159.8" x2="238" y2="159.8"/><line x1="58" y1="186.2" x2="238" y2="186.2"/>
      <line x1="58" y1="212.6" x2="238" y2="212.6"/>
    </g>
    <line x1="58" y1="239" x2="238" y2="239" stroke="#888" stroke-width="1"/>
    <g font-family="Lato, Arial, sans-serif" font-size="12" fill="#222" text-anchor="end">
      <text x="47" y="111">5</text><text x="47" y="137">4</text><text x="47" y="164">3</text>
      <text x="47" y="190">2</text><text x="47" y="217">1</text><text x="47" y="243">0</text>
    </g>
    <g fill="#4a7fc8">
      <rect x="68" y="125.5" width="11" height="113.5"/><rect x="114" y="173" width="11" height="66"/>
      <rect x="161" y="146.6" width="11" height="92.4"/><rect x="203" y="120.2" width="11" height="118.8"/>
    </g>
    <g fill="#e8262b">
      <rect x="79" y="175.6" width="11" height="63.4"/><rect x="125" y="122.8" width="11" height="116.2"/>
      <rect x="172" y="191.5" width="11" height="47.5"/><rect x="214" y="165.1" width="11" height="73.9"/>
    </g>
    <g font-family="Lato, Arial, sans-serif" font-size="8.5" fill="#222" text-anchor="middle">
      <text x="85" y="257">Category 1</text><text x="131" y="257">Category 2</text>
      <text x="175" y="257">Category 3</text><text x="219" y="257">Category 4</text>
    </g>
    <rect x="254" y="169" width="5" height="5" fill="#4a7fc8"/>
    <rect x="254" y="186" width="5" height="5" fill="#e8262b"/>
    <g font-family="Lato, Arial, sans-serif" font-size="8.5" fill="#222">
      <text x="262" y="175">Series 1</text><text x="262" y="192">Series 2</text>
    </g>
  </svg>
  <div class="feature" style="top:108px">
    <div class="feature__title"><span class="feature__icon feature__icon--blue"></span>Good or service:</div>
    <p class="feature__text">that is new or significantly improved. This includes significant improvements in technical</p>
  </div>
  <div class="feature" style="top:218px">
    <div class="feature__title"><span class="feature__icon feature__icon--red"></span>Good or service:</div>
    <p class="feature__text">that is new or significantly improved. This includes significant improvements in technical</p>
  </div>
  <footer class="footer-band">
    <span class="footer-band__url">www. quorvane-assoc.net</span>
    <span class="footer-band__brand"><span class="brand"><span class="brand__dot"></span>VELTARA</span></span>
  </footer>
</section>

<section class="slide slide--closing">
  <div class="closing-brand">
    <div class="brand"><span class="brand__dot"></span>VELTARA COLLECTIVE</div>
  </div>
  <h2 class="thank-you">THANK YOU</h2>
  <p class="presenter">Name of the presenter</p>
  <address class="contact">
    <span class="contact__label">Contact us:</span><br>
    Your Company Name<br>
    Followed by any streets<br>
    Your phone no: 0831 470218<br>
    Your fax no: 414 309871
  </address>
  <footer class="footer-band" style="height:45px">
    <span class="footer-band__url" style="top:14px">www. quorvane-assoc.net</span>
    <span class="footer-band__brand"><span class="brand"><span class="brand__dot"></span>VELTARA</span></span>
  </footer>
</section>

</body>
</html>
```